Business Card, Stationary, Brochure Template, Flyer Template
Templates need to be provided in Microsoft Publisher format as well as industry standards
Business Card, Stationary, Brochure Template, Flyer Template - Entertainment
Creative Brief
Use specific fonts
Font choice up to designer
Professional
Martin Hollowes
Managing Director
Unit Farrowby B Elmstead Court Redgate Lane Ashcombe St Peter Wiltshire SN14 8QT, UK
martin.hollowes@brightquill.co.uk
www.brightquill.co.uk
The Business cards designs need to be to the UK standard size 90cm by 55cm not the US standard shown in the brief. The business cards and Stationary need to have our company logo. The Brochure and Flyer template need to work with both our company logo and our product logo. For the Brochure and Flyer templates we are looking for a design that works along with our Stationary, we only require a template design something like these http://www.pagemoldery.com/Templates/Free-Templates/Free-Sample-Brochure-Template-Design.aspx and http://www.pagemoldery.com/Templates/Free-Templates/Free-Sample-Flyer-Template-Design.aspx but obviously unique to us and matching the other designs.

```html
<!DOCTYPE html>
<html lang="en">
<head>
<meta charset="utf-8">
<title>brightquill business cards</title>
<link href="https://fonts.googleapis.com/css2?family=Arimo:wght@400;700&display=swap" rel="stylesheet">
<style>
  :root {
    --bg: #e6e4e1;
    --card-top: #ffffff;
    --card-bottom: #e9e9ea;
    --ink: #3b3b3d;
    --ink-soft: #555558;
    --swoosh-dark: #4a4a4d;
    --swoosh-light: #9a9a9d;
    --accent-red: #d7262c;
    --accent-blue: #1f74c2;
    --accent-green: #3a9b35;
    --mark: #4b4b4f;
  }
  * { margin: 0; padding: 0; box-sizing: border-box; }
  html, body { width: 1200px; height: 691px; overflow: hidden; }
  body { background: var(--bg); font-family: "Arimo", Arial, sans-serif; color: var(--ink); position: relative; }

  .card {
    position: absolute; width: 420px; height: 258px; border-radius: 14px; overflow: hidden;
    background: linear-gradient(180deg, var(--card-top) 0%, var(--card-bottom) 100%);
    box-shadow: 0 3px 10px rgba(0,0,0,.18);
  }
  .card--front-red { left: 149px; top: 100px; --accent: var(--accent-red); }
  .card--back { left: 600px; top: 100px; }
  .card--front-blue { left: 149px; top: 384px; --accent: var(--accent-blue); }
  .card--front-green { left: 600px; top: 384px; --accent: var(--accent-green); }

  .brand { position: absolute; left: 34px; top: 30px; display: flex; align-items: center; gap: 9px; }
  .brand__square { width: 22px; height: 22px; background: var(--mark); }
  .brand__name { font-weight: 700; font-size: 27px; letter-spacing: -0.5px; color: var(--ink); line-height: 1; }

  .person { position: absolute; left: 34px; top: 112px; }
  .person__name { font-weight: 700; font-size: 13px; color: var(--ink); }
  .person__role { font-size: 10.5px; color: var(--ink-soft); margin-top: 2px; }
  .card--front-blue .person__name, .card--front-green .person__name { font-size: 15px; }
  .card--front-blue .person__role, .card--front-green .person__role { color: var(--accent); font-weight: 700; }

  .address { position: absolute; left: 196px; top: 104px; font-size: 8.2px; line-height: 1.35; color: var(--ink-soft); width: 200px; }
  .contacts { position: absolute; left: 196px; top: 146px; font-size: 8.2px; line-height: 1.45; color: var(--ink-soft); }
  .contacts dt { float: left; clear: left; width: 36px; font-weight: 700; color: var(--ink); }
  .contacts dd { margin-left: 36px; }

  .swoosh { position: absolute; left: 0; top: 0; width: 420px; height: 258px; }
  .web { position: absolute; left: 58px; bottom: 20px; font-size: 9px; color: #fff; }

  .back-brand { position: absolute; left: 0; right: 0; top: 98px; display: flex; justify-content: center; align-items: center; gap: 10px; }
  .back-brand .brand__square { width: 26px; height: 26px; }
  .back-brand .brand__name { font-size: 30px; }
  .back-web { position: absolute; left: 0; right: 0; top: 208px; text-align: center; font-size: 9.5px; color: var(--ink); }
</style>
</head>
<body>

<article class="card card--front-red">
  <svg class="swoosh" viewBox="0 0 420 258" aria-hidden="true">
    <defs>
      <linearGradient id="swRed" x1="0" y1="0" x2="1" y2="0">
        <stop offset="0" stop-color="#3f3f42"/><stop offset=".55" stop-color="#6d6d70"/><stop offset="1" stop-color="#a9a9ac"/>
      </linearGradient>
    </defs>
    <path d="M0 212 C110 178 250 232 420 178 L420 258 L0 258 Z" fill="url(#swRed)"/>
    <path d="M0 212 C110 178 250 232 420 178" fill="none" stroke="var(--accent-red)" stroke-width="3"/>
    <path d="M0 220 C120 188 260 238 420 186" fill="none" stroke="#ffffff" stroke-opacity=".35" stroke-width="1.5"/>
  </svg>
  <div class="brand"><span class="brand__square"></span><span class="brand__name">brightquill</span></div>
  <div class="person"><p class="person__name">Martin Hollowes</p><p class="person__role">Managing Director</p></div>
  <p class="address">Unit Farrowby B Elmstead Court<br>Redgate Lane, Ashcombe St Peter<br>Wiltshire, SN14 8QT, UK</p>
  <dl class="contacts">
    <dt>Phone</dt><dd>+44 (0)1632 960123</dd>
    <dt>Cell</dt><dd>+44 (0)7700 900456</dd>
    <dt>Fax</dt><dd>+44 (0)1632 960789</dd>
    <dt>Email</dt><dd>martin.hollowes@brightquill.co.uk</dd>
  </dl>
  <p class="web">www.brightquill.co.uk</p>
</article>

<article class="card card--back">
  <svg class="swoosh" viewBox="0 0 420 258" aria-hidden="true">
    <defs>
      <linearGradient id="swBack" x1="0" y1="0" x2="1" y2="0">
        <stop offset="0" stop-color="#bdbdc0"/><stop offset="1" stop-color="#e2e2e4"/>
      </linearGradient>
    </defs>
    <path d="M0 226 C130 200 270 248 420 206 L420 258 L0 258 Z" fill="url(#swBack)" opacity=".6"/>
  </svg>
  <div class="back-brand"><span class="brand__square"></span><span class="brand__name">brightquill</span></div>
  <p class="back-web">www.brightquill.co.uk</p>
</article>

<article class="card card--front-blue">
  <svg class="swoosh" viewBox="0 0 420 258" aria-hidden="true">
    <defs>
      <linearGradient id="swBlue" x1="0" y1="0" x2="1" y2="0">
        <stop offset="0" stop-color="#3f3f42"/><stop offset=".55" stop-color="#6d6d70"/><stop offset="1" stop-color="#a9a9ac"/>
      </linearGradient>
    </defs>
    <path d="M0 212 C110 178 250 232 420 178 L420 258 L0 258 Z" fill="url(#swBlue)"/>
    <path d="M0 212 C110 178 250 232 420 178" fill="none" stroke="var(--accent-blue)" stroke-width="3"/>
    <path d="M0 220 C120 188 260 238 420 186" fill="none" stroke="#ffffff" stroke-opacity=".35" stroke-width="1.5"/>
  </svg>
  <div class="brand"><span class="brand__square"></span><span class="brand__name">brightquill</span></div>
  <div class="person"><p class="person__name">Martin Hollowes</p><p class="person__role">Managing Director</p></div>
  <p class="address">Unit Farrowby B Elmstead Court<br>Redgate Lane, Ashcombe St Peter<br>Wiltshire, SN14 8QT, UK</p>
  <dl class="contacts">
    <dt>Phone</dt><dd>+44 (0)1632 960123</dd>
    <dt>Cell</dt><dd>+44 (0)7700 900456</dd>
    <dt>Fax</dt><dd>+44 (0)1632 960789</dd>
    <dt>Email</dt><dd>martin.hollowes@brightquill.co.uk</dd>
  </dl>
  <p class="web">www.brightquill.co.uk</p>
</article>

<article class="card card--front-green">
  <svg class="swoosh" viewBox="0 0 420 258" aria-hidden="true">
    <defs>
      <linearGradient id="swGreen" x1="0" y1="0" x2="1" y2="0">
        <stop offset="0" stop-color="#3f3f42"/><stop offset=".55" stop-color="#6d6d70"/><stop offset="1" stop-color="#a9a9ac"/>
      </linearGradient>
    </defs>
    <path d="M0 212 C110 178 250 232 420 178 L420 258 L0 258 Z" fill="url(#swGreen)"/>
    <path d="M0 212 C110 178 250 232 420 178" fill="none" stroke="var(--accent-green)" stroke-width="3"/>
    <path d="M0 220 C120 188 260 238 420 186" fill="none" stroke="#ffffff" stroke-opacity=".35" stroke-width="1.5"/>
  </svg>
  <div class="brand"><span class="brand__square"></span><span class="brand__name">brightquill</span></div>
  <div class="person"><p class="person__name">Martin Hollowes</p><p class="person__role">Managing Director</p></div>
  <p class="address">Unit Farrowby B Elmstead Court<br>Redgate Lane, Ashcombe St Peter<br>Wiltshire, SN14 8QT, UK</p>
  <dl class="contacts">
    <dt>Phone</dt><dd>+44 (0)1632 960123</dd>
    <dt>Cell</dt><dd>+44 (0)7700 900456</dd>
    <dt>Fax</dt><dd>+44 (0)1632 960789</dd>
    <dt>Email</dt><dd>martin.hollowes@brightquill.co.uk</dd>
  </dl>
  <p class="web">www.brightquill.co.uk</p>
</article>

</body>
</html>
```